looking for sleek business card to standout from the crowd!

We are a young biotechnology company looking to help you personalize your health through understanding your genetic make up. We need you help in making a clean but sleek business card design using our new logo. The goal? Any time we give our cards out, people say "nice card!" The feel we are going for is "modern-techy". We don't want to come across as an old, giant pharma company, but not trying to be a hipster either.

Target Market(s)

healthcare and biotechnology industry.

Industry/Entity Type

Biotechnology

Contact Information for Business Card

Info to include on the card will be NAME, TITLE, EMAIL, PHONE. The companies website (www.corvalinbio.com) should also be on the card some where. Would like the logo, when printed, to be raised.

Requirements
Must have
• The logo we have attached in the color it is in. Fonts for text should lean toward more professional/tech.
Nice to have
• Prefer white/light color background
Should not have
• cartoons, landscape backgrounds images.

```html
<!DOCTYPE html>
<html lang="en">
<head>
<meta charset="utf-8">
<title>Corvalin Business Card</title>
<link href="https://fonts.googleapis.com/css2?family=Lato:wght@400;700&display=swap" rel="stylesheet">
<style>
  :root {
    --bg: #6b767d;
    --card: #ffffff;
    --brand-blue: #1a6fc0;
    --ink: #222222;
  }
  * { margin: 0; padding: 0; box-sizing: border-box; }
  html, body {
    width: 1200px; height: 900px; overflow: hidden;
    background: var(--bg);
    font-family: "Lato", sans-serif;
  }
  .stage {
    width: 1200px; height: 900px;
    display: flex; align-items: center; justify-content: center;
  }
  .card {
    position: relative;
    width: 840px; height: 480px;
    background: var(--card);
    overflow: hidden;
  }
  .card__tab {
    position: absolute;
    left: 0; top: 300px;
    width: 22px; height: 44px;
    background: var(--brand-blue);
    border-radius: 0 8px 8px 0;
  }
  .brand {
    position: absolute;
    left: 70px; top: 72px;
  }
  .brand__name {
    font-weight: 700;
    font-size: 50px;
    letter-spacing: 2px;
    color: var(--brand-blue);
  }
  .person {
    position: absolute;
    left: 330px; top: 230px;
  }
  .person__name {
    font-weight: 700; font-size: 22px;
    letter-spacing: 0.5px;
    color: var(--brand-blue);
  }
  .person__title {
    font-size: 19px; color: var(--ink); margin-top: 2px;
  }
  .contact {
    position: absolute;
    left: 380px; top: 318px;
    list-style: none;
  }
  .contact__item {
    display: flex; align-items: center; gap: 14px;
    font-size: 19px; color: var(--ink);
    line-height: 30px;
  }
  .contact__icon { width: 18px; height: 18px; flex: none; }
</style>
</head>
<body>
<main class="stage">
  <article class="card">
    <div class="card__tab"></div>

    <div class="brand">
      <span class="brand__name">CORVALIN</span>
    </div>

    <div class="person">
      <p class="person__name">MARLOW DACEY</p>
      <p class="person__title">Owner</p>
    </div>

    <ul class="contact">
      <li class="contact__item">
        <svg class="contact__icon" viewBox="0 0 24 24" fill="var(--brand-blue)"><path d="M6.6 10.8a15 15 0 0 0 6.6 6.6l2.2-2.2a1 1 0 0 1 1-.25 11.4 11.4 0 0 0 3.6.57 1 1 0 0 1 1 1V20a1 1 0 0 1-1 1A17 17 0 0 1 3 4a1 1 0 0 1 1-1h3.5a1 1 0 0 1 1 1c0 1.25.2 2.45.57 3.57a1 1 0 0 1-.25 1z"/></svg>
        <span>555-018-274</span>
      </li>
      <li class="contact__item">
        <svg class="contact__icon" viewBox="0 0 24 24" fill="none" stroke="var(--brand-blue)" stroke-width="2"><rect x="6" y="2" width="12" height="20" rx="2"/><line x1="11" y1="18" x2="13" y2="18"/></svg>
        <span>555-094-617</span>
      </li>
      <li class="contact__item">
        <svg class="contact__icon" viewBox="0 0 24 24"><rect x="2" y="5" width="20" height="14" fill="var(--brand-blue)"/><path d="M2 5l10 8 10-8" fill="none" stroke="#fff" stroke-width="1.6"/></svg>
        <span>hello@corvalinbio.com</span>
      </li>
      <li class="contact__item">
        <svg class="contact__icon" viewBox="0 0 24 24" fill="none" stroke="var(--brand-blue)" stroke-width="2"><circle cx="12" cy="12" r="9"/><path d="M3 12h18M12 3c3 3 3 15 0 18M12 3c-3 3-3 15 0 18"/></svg>
        <span>www.corvalinbio.com</span>
      </li>
    </ul>
  </article>
</main>
</body>
</html>
```